Pelranosky Bee Farm Family owned and operated

We are family owned and operated Bee Farm located in Anderson SC. Our honey is Completely Raw and Natural. We do not use any chemicals with our bees and we do not feed our bees, leaving them their own honey to feed on. Honey is never heated and is only coarse filtered. We are certified South Carolina Producer. Along with Honey we do sell:• 100% Beeswax• Beeswax Candles• Raw Pollen • and Unprocessed Propolis
Updates

Target Market(s)

wholesale- retail ,farmers markets, Festival,bazaars,holiday markets.

Industry/Entity Type

Farmer

Font styles to use
Decorative
Script

Colors
fece3e
f68d4d
f04a50

Requirements
Must have
• Raw, Unfiltered, unprocessed honey,, honeycomb, raw bee pollen, propolis, beeswax candles, Lip balm, 5 frame nucks and queens.
Nice to have
• Our Calvine honey we harvested on Tindle Ridge @ elevation of 3,500ft, that is the highest point in SC. We are 3rd generation beekeepers, inhereted love for bees and old fashion ways of keeping/ caring for bees. Originally from Uzbeckistan, but last 25 years in USA. we are at local farmers markets where you can taste/sample honey.

```html
<!DOCTYPE html>
<html lang="en">
<head>
<meta charset="utf-8">
<title>Pelranosky Bee Farm – Trifold Brochure</title>
<link href="https://fonts.googleapis.com/css2?family=Noto+Serif:wght@400;700&family=Lora:wght@400;700&display=swap" rel="stylesheet">
<style>
:root{
  --stage:#e9e9e9;
  --paper:#ffffff;
  --honey:#fdc82f;
  --cream:#fdf1d2;
  --bark:#8b3a14;
  --ink:#3a2616;
  --heading:#2a1a0c;
}
*{margin:0;padding:0;box-sizing:border-box}
html,body{width:900px;height:1200px;overflow:hidden}
body{background:var(--stage);position:relative;font-family:"Lora",serif;color:var(--ink)}
.spread{position:absolute;left:90px;width:720px;height:557px;background:var(--paper);box-shadow:6px 6px 8px rgba(0,0,0,.25);overflow:hidden}
.spread--outside{top:28px}
.spread--inside{top:608px}
.abs{position:absolute}
.shape{position:absolute;left:0;top:0}
.photo{position:absolute}
.title{font-family:"Noto Serif",serif;font-weight:700;color:var(--heading)}
p{font-size:10.5px;line-height:1.3}
.justify{text-align:justify}
.center{text-align:center}
.right{text-align:right}
.products li{list-style:none;font-family:"Noto Serif",serif;font-weight:700;font-size:10.5px;line-height:13px;color:var(--heading)}
.social{display:flex;flex-direction:column;align-items:center;gap:2px;font-size:10.5px}
.social-mark{width:22px;height:22px;background:var(--bark)}
.social-mark--round{border-radius:50%}
.caption-bar{background:var(--honey);font-style:italic;font-size:8px;text-align:center;line-height:22px}
.framed{border:4px solid #fff;box-shadow:1px 2px 4px rgba(0,0,0,.35)}
.about-text{font-size:10px;line-height:13px;letter-spacing:-.1px}
</style>
</head>
<body>

<section class="spread spread--outside">
  <svg class="shape" width="720" height="557" viewBox="0 0 720 557" aria-hidden="true">
    <path d="M0 0H240V0C230 60 150 80 60 95C30 100 10 110 0 120Z" fill="var(--honey)"/>
    <path d="M240 0C236 55 160 82 70 98" fill="none" stroke="var(--bark)" stroke-width="5"/>
    <rect x="240" y="60" width="243" height="178" fill="var(--honey)"/>
    <rect x="240" y="238" width="243" height="7" fill="var(--bark)"/>
    <path d="M483 0H720V55C650 70 580 55 520 78C500 85 490 95 483 100Z" fill="var(--honey)"/>
    <path d="M483 100C520 70 580 62 640 62C680 60 705 55 720 50" fill="none" stroke="var(--bark)" stroke-width="6"/>
    <path d="M483 398C540 355 640 350 720 372V557H483Z" fill="var(--honey)"/>
    <path d="M483 398C540 355 640 350 720 372" fill="none" stroke="var(--bark)" stroke-width="6"/>
  </svg>

  <h2 class="title abs" style="left:17px;top:30px;font-size:15px;line-height:19px">Pure Beeswax<br>Candles</h2>
  <div class="photo" role="img" aria-label="Lit beeswax pillar candles glowing in the dark" style="left:0;top:122px;width:148px;height:290px;background:linear-gradient(160deg,#5a1a10,#2a0c06 55%,#d88a3a);clip-path:path('M0 0C50 0 85 30 92 80L96 140L148 190L148 290L0 290Z')"></div>
  <div class="photo framed" role="img" aria-label="Flower-shaped yellow beeswax candle" style="left:102px;top:258px;width:130px;height:115px;background:radial-gradient(circle,#f3c54a,#c99020);transform:rotate(-8deg)"></div>
  <p class="abs right" style="left:98px;top:144px;width:132px;font-size:10px;line-height:12.5px">All our candles are made of 100% natural beeswax and are chemical free. This beeswax is produced by our bees and it has a vibrant color and a wonderfully delicious honey scent.</p>
  <p class="abs justify" style="left:17px;top:424px;width:213px">Beeswax burns brighter, longer, and cleaner than any other candle material. Beeswax candle flames emit the full spectrum of light and release negative ions that improve air quality, stimulate the pituitary gland, and enhance health and vitality.</p>

  <h2 class="title abs" style="left:265px;top:30px;font-size:15px">Contact Us</h2>
  <div class="abs center" style="left:240px;top:84px;width:243px">
    <div class="title" style="font-size:15px">Marek Pelranosky</div>
    <p style="font-size:10.5px;line-height:12px">872 Hollis Rd Anderson<br>SC 29621<br>Phone: 864.555.0142</p>
  </div>
  <div class="photo" role="img" aria-label="Gift basket of honey jars tied with a red ribbon" style="left:302px;top:150px;width:118px;height:168px;border-radius:50%;border:4px solid #fff;background:radial-gradient(circle at 50% 40%,#c44a2a,#7a4a20 55%,#c79a58)"></div>
  <div class="social abs" style="left:240px;top:322px;width:243px">
    <span class="social-mark social-mark--round"></span>
    <span>Pelranosky-Bee-Farm</span>
    <span class="social-mark" style="margin-top:2px"></span>
    <span>pelranosky_beefarm</span>
  </div>
  <div class="photo" role="img" aria-label="Two children among wildflowers in a meadow" style="left:240px;top:410px;width:243px;height:147px;background:linear-gradient(180deg,#b9c9e0,#8aa670 50%,#5a8a3a);clip-path:path('M0 20C60 -5 130 15 243 25V147H0Z')"></div>

  <div class="abs center" style="left:483px;top:104px;width:237px">
    <h1 class="title" style="font-size:26px;line-height:28px">Pelranosky</h1>
    <div class="title" style="font-size:14px">Bee Farm</div>
  </div>
  <div class="photo" role="img" aria-label="Bowl of honey with a dipper beside beeswax candles" style="left:483px;top:165px;width:237px;height:137px;background:linear-gradient(180deg,#8a3a2a,#c78a2a 45%,#d49a30 75%,#d8c8a0)"></div>
  <p class="abs center title" style="left:483px;top:316px;width:237px;font-size:10.5px;color:var(--bark);line-height:12px">a family owned bee farm<br>operated &amp; located in Anderson SC</p>
  <ul class="products abs center" style="left:483px;top:427px;width:237px">
    <li>Raw, Unfiltered, Unprocessed Honey</li>
    <li>Honeycomb</li>
    <li>Raw Bee Pollen</li>
    <li>Propolis</li>
    <li>Beeswax Candles</li>
    <li>Lip Balm</li>
    <li>5 Frame Nucks and Queens</li>
  </ul>
</section>

<section class="spread spread--inside">
  <svg class="shape" width="720" height="557" viewBox="0 0 720 557" aria-hidden="true">
    <path d="M0 0H240V8C190 70 90 80 0 82Z" fill="var(--honey)"/>
    <path d="M0 82C90 80 190 70 240 8" fill="none" stroke="var(--bark)" stroke-width="5"/>
    <rect x="245" y="0" width="238" height="148" fill="var(--cream)"/>
    <rect x="245" y="148" width="238" height="6" fill="var(--honey)"/>
    <path d="M483 0H720V20C700 80 560 75 483 92Z" fill="var(--honey)"/>
    <path d="M483 92C560 75 700 80 720 20" fill="none" stroke="var(--bark)" stroke-width="5"/>
  </svg>

  <div class="abs center" style="left:40px;top:26px;width:140px">
    <h2 class="title" style="font-size:16px">About Us</h2>
    <div style="font-size:11px">Pelranosky Bee Farm</div>
  </div>
  <p class="abs about-text" style="left:17px;top:106px;width:215px">We are a 3 rd generation of beekeepers that, inherited the love for bees and old fashion ways to care for them. Family owned and operated, here in Anderson SC. Our honey is Completely Raw and Natural.</p>
  <div class="photo" role="img" aria-label="Farm stand displaying honey jars in front of a building" style="left:17px;top:186px;width:211px;height:206px;background:linear-gradient(180deg,#8fa870,#6a8a50 30%,#b8863a 60%,#c7773a)"></div>
  <p class="abs about-text" style="left:17px;top:402px;width:215px">We do not use any chemicals with our bees and we do not feed our bees, leaving them their own honey to feed on. Honey is never heated and is only coarse filtered. We are certified South Carolina Producer.</p>
  <div class="photo" role="img" aria-label="Row of colorful beehives in a field" style="left:17px;top:480px;width:211px;height:62px;background:linear-gradient(180deg,#c8d8c0,#b08ac0 55%,#8a9a60)"></div>

  <h3 class="title abs" style="left:260px;top:22px;font-size:9px">The Calvine Honey</h3>
  <div class="photo" role="img" aria-label="Flowering tree branch" style="left:260px;top:40px;width:78px;height:75px;background:linear-gradient(135deg,#4a7a3a,#9ab870)"></div>
  <p class="abs justify" style="left:344px;top:40px;width:131px;font-size:7.5px;line-height:9px">Calvine trees bloom from mid June to late July in mountains, where we move our beehives. Under favorable conditions the nectar is so abundant; it can be shaken from the blooms in small drops. Calvine Honey is one of the most favorable honeys in the world, winning best tasting honey in the world 2 times.</p>
  <div class="photo" role="img" aria-label="Beehives beside a pond in the woods" style="left:257px;top:162px;width:100px;height:100px;background:linear-gradient(180deg,#6a8a4a,#3a5a3a 60%,#7a8a9a)"></div>
  <div class="photo" role="img" aria-label="Beehives in a snowy yard" style="left:368px;top:162px;width:100px;height:100px;background:linear-gradient(180deg,#7a7a60,#b8a890 50%,#e8e8ec)"></div>
  <div class="photo" role="img" aria-label="Family inspecting a hive frame" style="left:257px;top:272px;width:211px;height:143px;background:linear-gradient(160deg,#6a6a5a,#a89a8a 50%,#5a4a30)"></div>
  <div class="photo" role="img" aria-label="Close view of golden honeycomb" style="left:257px;top:425px;width:211px;height:117px;background:linear-gradient(180deg,#5a7a3a,#e8d8a0 45%,#d8a040)"></div>
  <div class="caption-bar abs" style="left:245px;top:507px;width:235px;height:22px">The Purest, Rich Honey</div>

  <div class="abs center" style="left:535px;top:26px;width:140px">
    <h2 class="title" style="font-size:16px">Our Products</h2>
    <div style="font-size:11px">Pelranosky Bee Farm</div>
  </div>
  <div class="photo framed" role="img" aria-label="Honey jars and candles on a market table" style="left:500px;top:112px;width:158px;height:145px;background:linear-gradient(180deg,#8a9aa0,#c87a30 50%,#e8b030)"></div>
  <div class="photo framed" role="img" aria-label="Beeswax candles" style="left:655px;top:70px;width:80px;height:70px;background:linear-gradient(135deg,#c8a040,#7a5a20);transform:rotate(8deg)"></div>
  <div class="photo framed" role="img" aria-label="Woven baskets with beeswax" style="left:648px;top:150px;width:72px;height:110px;background:linear-gradient(180deg,#b8905a,#7a5a30);transform:rotate(-6deg)"></div>
  <div class="photo framed" role="img" aria-label="Jars of honey with red lids" style="left:500px;top:255px;width:80px;height:82px;background:linear-gradient(180deg,#3a3a2a,#c04020 50%,#e8a030);transform:rotate(-4deg)"></div>
  <div class="photo framed" role="img" aria-label="Scoop of raw bee pollen" style="left:578px;top:245px;width:140px;height:92px;background:radial-gradient(circle at 55% 60%,#b8a030,#6a7a3a 60%,#d8d8d0);transform:rotate(-8deg)"></div>
  <p class="abs justify" style="left:510px;top:362px;width:200px;font-size:10px;line-height:13px">It is extremely aromatic, with a distinctive honey flavor of anise and spice and it crystallizes very slowly if not at all. There is <strong>no other honey like this.</strong></p>
  <div class="abs center" style="left:483px;top:427px;width:237px">
    <h2 class="title" style="font-size:16px">Call Us</h2>
    <div style="font-size:11px">Marek or Ilona</div>
    <div class="title" style="font-size:20px;margin-top:4px">864.555.0142</div>
  </div>
</section>

</body>
</html>
```